Scrap Metal Recycling

We are looking for a simple yet bold business card. We already have the logo, please see attached. Color scheme of blue, black and white or just blue and white.

```html
<!DOCTYPE html>
<html lang="en">
<head>
<meta charset="utf-8">
<title>Ridgeline Metals Inc. – Business Card</title>
<link rel="stylesheet" href="https://fonts.googleapis.com/css2?family=Inter:wght@400;500;700&display=swap">
<style>
  :root {
    --page-bg: #d9d6d1;
    --card-light: #e6e9ec;
    --card-light-edge: #c9d1d8;
    --panel-dark: #2a2b2d;
    --panel-dark-deep: #1b1c1d;
    --accent-blue: #1b5f82;
    --accent-blue-bright: #2377a3;
    --text-light: #d8d8d8;
    --text-ink: #1a1a1a;
    --tagline: #184e66;
  }
  * { margin: 0; padding: 0; box-sizing: border-box; }
  html, body {
    width: 1200px; height: 969px; overflow: hidden;
    background: var(--page-bg);
    font-family: "Inter", Arial, sans-serif;
  }
  .business-card {
    position: absolute; left: 120px; top: 210px;
    width: 960px; height: 548px;
    border-radius: 26px; overflow: hidden;
    background: radial-gradient(ellipse at 70% 45%, var(--card-light), var(--card-light-edge));
    box-shadow: 0 10px 30px rgba(0,0,0,0.18);
  }
  .card-shapes { position: absolute; inset: 0; }
  .contact-block { position: absolute; left: 69px; top: 102px; color: var(--text-light); }
  .person-name {
    font-size: 31px; font-weight: 500; letter-spacing: 0.3px;
    color: var(--accent-blue-bright); line-height: 1.1;
  }
  .person-role { font-size: 21px; margin-top: 4px; }
  .address { font-size: 21px; line-height: 27px; margin-top: 56px; letter-spacing: 0.3px; }
  .contact-list { list-style: none; margin-top: 6px; }
  .contact-list li {
    display: flex; align-items: center; gap: 12px;
    font-size: 22px; line-height: 27.5px; letter-spacing: 0.3px;
  }
  .contact-list svg { width: 17px; height: 17px; flex: none; fill: var(--accent-blue); }
  .brand-lockup { position: absolute; left: 502px; top: 248px; text-align: left; }
  .brand-name {
    display: flex; align-items: center; gap: 12px;
    font-size: 38px; font-weight: 700; color: var(--text-ink); letter-spacing: -0.5px;
  }
  .brand-dot { width: 22px; height: 22px; border-radius: 50%; background: var(--text-ink); }
  .brand-tagline {
    margin-top: 6px; font-size: 19px; font-weight: 500;
    letter-spacing: 4.6px; color: var(--tagline);
  }
</style>
</head>
<body>
  <div class="business-card">
    <svg class="card-shapes" viewBox="0 0 960 548" width="960" height="548" aria-hidden="true">
      <defs>
        <linearGradient id="panelShade" x1="0" y1="0" x2="0.6" y2="1">
          <stop offset="0" stop-color="var(--panel-dark)"/>
          <stop offset="1" stop-color="var(--panel-dark-deep)"/>
        </linearGradient>
      </defs>
      <path class="dark-panel" fill="url(#panelShade)"
            d="M0 0 H494 C420 60 380 180 398 290 C418 400 520 490 618 548 H0 Z"/>
      <path class="accent-swoosh" fill="var(--accent-blue)"
            d="M486 20 C410 110 382 240 402 340 C428 440 520 505 618 548 H574 C490 500 410 430 392 345 C372 250 400 120 486 20 Z"/>
    </svg>

    <div class="contact-block">
      <h1 class="person-name">DANIEL HARROW</h1>
      <p class="person-role">President</p>
      <p class="address">4120 Cedar Bend Road<br>Juneau,<br>Alaska 34512</p>
      <ul class="contact-list">
        <li><svg viewBox="0 0 24 24"><path d="M6.6 10.8a15 15 0 0 0 6.6 6.6l2.2-2.2a1 1 0 0 1 1-.25 11.4 11.4 0 0 0 3.6.57 1 1 0 0 1 1 1V20a1 1 0 0 1-1 1A17 17 0 0 1 3 4a1 1 0 0 1 1-1h3.5a1 1 0 0 1 1 1c0 1.25.2 2.45.57 3.6a1 1 0 0 1-.25 1z"/></svg>555-214-7730</li>
        <li><svg viewBox="0 0 24 24"><path d="M7 2h10a2 2 0 0 1 2 2v16a2 2 0 0 1-2 2H7a2 2 0 0 1-2-2V4a2 2 0 0 1 2-2zm0 3v13h10V5z"/></svg>555-508-1946</li>
        <li><svg viewBox="0 0 24 24"><path d="M7 3h10v5H7zM4 9h16a2 2 0 0 1 2 2v6h-4v4H6v-4H2v-6a2 2 0 0 1 2-2zm4 7v3h8v-3z"/></svg>555-362-4081</li>
        <li><svg viewBox="0 0 24 24"><path d="M3 5h18v14H3zm2 2v.5l7 4.5 7-4.5V7l-7 4.5z"/></svg>info@ridgelinemetals.com</li>
        <li><svg viewBox="0 0 24 24"><circle cx="12" cy="12" r="10"/></svg>www.ridgelinemetals.com</li>
      </ul>
    </div>

    <div class="brand-lockup">
      <p class="brand-name"><span class="brand-dot"></span>Ridgeline Metals Inc.</p>
      <p class="brand-tagline">SCRAP METAL RECYCLING</p>
    </div>
  </div>
</body>
</html>
```